v-orn design for startup inpection service

building and pest inspections what i had in mind was v-orn in large print with prepurchase in small print directly under it and the small tm (tradmark) .Within the C I would like an eye but I don't want to take away from the C so maybe the eye would be done in a fine line?I would also like the Building and Pest inspections to be prominent and large .Have no idea of colors but do like black orange and silver

Target Market(s)

home buyers and realestate agents

Industry/Entity Type

Building

Contact Information for Business Card

v-orn prepurchase, Phone 0417382951, fax 02 93147708, email v-orn@mailbay.com.au ,building and pest inspections

Font styles to use
Sans Serif

Requirements
Must have
• bold color
• simple layout
• bold color
• uncluttered layout
Should not have
• contact details the same size as Building and Pest Inspections

```html
<!DOCTYPE html>
<html lang="en">
<head>
<meta charset="utf-8">
<title>V-orn Building and Pest Inspections – Business Card</title>
<link rel="stylesheet" href="https://fonts.googleapis.com/css2?family=Ubuntu:wght@400;500;700&display=swap">
<style>
  :root {
    --white: #ffffff;
    --brand-blue: #0a2fa0;
    --night: #0b1522;
    --band-phone: #0c4f8c;
    --band-fax: #55ccfb;
    --band-mail: #90f7fd;
    --band-foot: #ecfcfe;
    --ink: #0b1522;
  }
  html, body {
    margin: 0;
    padding: 0;
    width: 1200px;
    height: 686px;
    overflow: hidden;
    background: var(--white);
  }
  .card {
    position: relative;
    width: 1200px;
    height: 686px;
    font-family: "Ubuntu", sans-serif;
    background: var(--white);
  }
  .brand {
    position: absolute;
    left: 0;
    top: 0;
    width: 560px;
    height: 686px;
    display: flex;
    align-items: center;
    justify-content: center;
    gap: 22px;
  }
  .brand-dot {
    width: 112px;
    height: 112px;
    border-radius: 50%;
    background: var(--brand-blue);
  }
  .brand-name {
    font-size: 96px;
    font-weight: 700;
    color: var(--brand-blue);
    line-height: 1;
  }
  .info {
    position: absolute;
    left: 600px;
    top: 0;
    width: 600px;
    height: 686px;
  }
  .info-header {
    height: 229px;
    background: var(--night);
    color: var(--white);
    display: flex;
    flex-direction: column;
    align-items: center;
    justify-content: center;
    padding-bottom: 24px;
    box-sizing: border-box;
  }
  .company {
    font-size: 48px;
    font-weight: 700;
    line-height: 1.1;
  }
  .service {
    font-size: 40px;
    font-weight: 700;
    line-height: 1.25;
    white-space: nowrap;
  }
  .contact {
    height: 137px;
    display: flex;
    align-items: center;
    padding-left: 20px;
    box-sizing: border-box;
  }
  .contact-phone { background: var(--band-phone); color: var(--white); }
  .contact-fax { background: var(--band-fax); color: var(--ink); }
  .contact-mail { background: var(--band-mail); color: var(--ink); height: 139px; }
  .info-foot { height: 44px; background: var(--band-foot); }
  .contact-icon {
    width: 80px;
    height: 80px;
    flex: none;
  }
  .contact-text {
    margin-left: 37px;
    font-size: 32px;
    font-weight: 400;
    letter-spacing: 0.5px;
    white-space: nowrap;
  }
</style>
</head>
<body>
<div class="card">
  <div class="brand">
    <div class="brand-dot"></div>
    <div class="brand-name">V-orn</div>
  </div>

  <div class="info">
    <div class="info-header">
      <div class="company">V-orn</div>
      <div class="service">Building and Pest inspections</div>
    </div>

    <div class="contact contact-phone">
      <svg class="contact-icon" viewBox="0 0 80 80" aria-hidden="true">
        <circle cx="40" cy="40" r="37" fill="none" stroke="#ffffff" stroke-width="2.5"/>
        <path d="M36 22 h4 l2 10 h-4 q-2 8 0 16 h4 l-2 10 h-4 q-8 -18 0 -36 z" fill="#ffffff"/>
      </svg>
      <span class="contact-text">0417382951</span>
    </div>

    <div class="contact contact-fax">
      <svg class="contact-icon" viewBox="0 0 80 80" aria-hidden="true">
        <circle cx="40" cy="40" r="37" fill="none" stroke="#0b1522" stroke-width="2.5"/>
        <rect x="28" y="18" width="24" height="16" fill="#ffffff" stroke="#0c4f8c" stroke-width="2.5"/>
        <line x1="32" y1="24" x2="48" y2="24" stroke="#0c4f8c" stroke-width="2"/>
        <line x1="32" y1="29" x2="48" y2="29" stroke="#0c4f8c" stroke-width="2"/>
        <rect x="18" y="34" width="44" height="26" rx="3" fill="#0c4f8c"/>
        <path d="M28 54 q12 -8 24 0" fill="none" stroke="#ffffff" stroke-width="3"/>
      </svg>
      <span class="contact-text">02 93147708</span>
    </div>

    <div class="contact contact-mail">
      <svg class="contact-icon" viewBox="0 0 80 80" aria-hidden="true">
        <circle cx="40" cy="40" r="37" fill="none" stroke="#0b1522" stroke-width="2.5"/>
        <text x="40" y="55" text-anchor="middle" font-family="Ubuntu, sans-serif" font-size="46" font-weight="700" fill="#0b1522">@</text>
      </svg>
      <span class="contact-text">v-orn@mailbay.com.au</span>
    </div>

    <div class="info-foot"></div>
  </div>
</div>
</body>
</html>
```